Alcohol free flavoured Malt Drink Label design

we are beverage company producer our main brand is Brightwave, we are willing to produce Alcohol free flavoured Malt Drink, this product target new generation should be fresh colourful and modern, the name of the Malt drink is Zeal. so main brand is Brightwave and product name is ZEAL. the label size: 198mm X 66mm

Dear All
i changed the product name to NUR (means Crown ) this will add more ideas in the design . Thanks

```html
<!DOCTYPE html>
<html lang="en">
<head>
<meta charset="utf-8">
<title>NUR Flavoured Malt Drink – Label</title>
<link rel="stylesheet" href="https://fonts.googleapis.com/css2?family=Montserrat:wght@800&family=Montserrat+Alternates:wght@400;700&display=swap">
<style>
  :root {
    --backdrop: #7a746f;
    --label-white: #ffffff;
    --ink: #1b1b1b;
    --rose-light: #e3aaa9;
    --rose-mid: #cf8584;
    --rose-deep: #b76a69;
    --rose-shadow: #c0615f;
    --splash: #f3d3d0;
    --splash-fade: #fbeeed;
    --text-light: #fbf3f3;
  }
  * { margin: 0; padding: 0; box-sizing: border-box; }
  html, body {
    width: 1200px;
    height: 1198px;
    overflow: hidden;
    background: var(--backdrop);
  }
  .label {
    position: absolute;
    left: 50px;
    top: 415px;
    width: 1100px;
    height: 367px;
    background: var(--label-white);
    overflow: hidden;
  }
  .label__splash {
    position: absolute;
    top: 86px;
    height: 74px;
  }
  .label__splash--left {
    left: 0;
    width: 330px;
    border-radius: 0 40px 0 0;
    background: linear-gradient(90deg, var(--splash) 0%, var(--splash-fade) 100%);
  }
  .label__splash--right {
    right: 0;
    width: 380px;
    border-radius: 40px 0 0 0;
    background: linear-gradient(270deg, var(--splash) 0%, var(--splash-fade) 100%);
  }
  .label__brand {
    position: absolute;
    top: 44px;
    left: 0;
    width: 100%;
    text-align: center;
    font-family: "Montserrat Alternates", sans-serif;
    font-weight: 700;
    font-size: 58px;
    line-height: 1.2;
    letter-spacing: -1px;
    color: var(--ink);
  }
  .label__panel {
    position: absolute;
    left: 0;
    top: 160px;
    width: 100%;
    height: 207px;
    border-radius: 18px 18px 0 0;
    background: linear-gradient(90deg, var(--rose-light) 0%, var(--rose-mid) 45%, var(--rose-deep) 100%);
    text-align: center;
  }
  .label__product {
    display: block;
    padding-top: 22px;
    font-family: "Montserrat", sans-serif;
    font-weight: 800;
    font-size: 112px;
    line-height: 1;
    letter-spacing: 2px;
    color: var(--text-light);
    text-shadow: 5px 5px 0 var(--rose-shadow);
  }
  .label__descriptor {
    display: block;
    margin-top: 16px;
    font-family: "Montserrat Alternates", sans-serif;
    font-weight: 400;
    font-size: 28px;
    color: var(--text-light);
  }
</style>
</head>
<body>
  <main class="label">
    <div class="label__splash label__splash--left" role="img" aria-label="Pink liquid splash illustration"></div>
    <div class="label__splash label__splash--right" role="img" aria-label="Pink liquid splash illustration"></div>
    <div class="label__brand">Brightwave</div>
    <section class="label__panel">
      <span class="label__product">NUR</span>
      <span class="label__descriptor">Flavoured Malt Drink</span>
    </section>
  </main>
</body>
</html>
```